Technology Company Web Design Project - EXAMPLES

We are a technology company that is launching a mobile contactless voucher redemption, identification and loyalty solution. This technology is like NFC technology but is available now, and supported by all smartphones on the market.
We are looking for example designs for the website.
This website is to do a number of functions:

Explain the Technology ( SDK, Pod, Applications )
Explain the product features ( use cases )
Provide information on the company
Provide information for developers on the SDK.

I have attached a content map to show all of the areas the finished website should have.
All iam looking for at the moment is a homepage example and a content section example.

Brand guidelines are attached as well as more info on the technology.

Target Market(s)

Corporate, Retailers, Mobile Networks, FMCG brands

Requirements
Must have
• Have included content sections that need to be included and worked into a navigation.
Nice to have
• fat footer
carousel front page image.
Should not have
• THIS IS NOT A FULL WEB DESIGN - JUST EXAMPLE HOME PAGE AND CONTENT PAGE

```html
<!DOCTYPE html>
<html lang="en">
<head>
<meta charset="utf-8">
<title>tapnova – contactless redemption for mobile phones</title>
<link href="https://fonts.googleapis.com/css2?family=Source+Sans+3:wght@300;400;600;700&family=Arimo:wght@400;700&display=swap" rel="stylesheet">
<style>
:root{
  --blue:#12a6e3;
  --blue-dark:#0a8fcf;
  --ink:#3a3a3a;
  --text:#6a6a6a;
  --muted:#8a8a8a;
  --panel:#f3f3f3;
  --line:#dcdcdc;
  --footer:#2b2b2b;
  --footer-text:#a9a9a9;
  --white:#ffffff;
  --red:#e0464e;
}
*{margin:0;padding:0;box-sizing:border-box}
html,body{width:847px;height:1200px;overflow:hidden;background:var(--white)}
body{font-family:"Arimo",Arial,sans-serif;color:var(--text)}
.page{position:relative;width:847px;height:1200px}
.abs{position:absolute}
.brand{left:90px;top:10px;font-family:"Source Sans 3",sans-serif;font-size:48px;font-weight:400;color:#3d3d3d;letter-spacing:-1px;line-height:56px}
.brand sup{font-size:9px;vertical-align:top;position:relative;top:8px;left:2px;letter-spacing:0}
.tagline{left:92px;top:72px;font-size:9.5px;color:var(--blue)}
.tagline b{font-weight:700}
.search{left:543px;top:38px;width:212px;height:20px;border:1px solid #c9c9c9;border-radius:4px;background:linear-gradient(#f2f2f2,#fff);font-size:9px;font-style:italic;color:#888;padding:4px 9px}
.search-btn{left:729px;top:38px;width:26px;height:20px;border-radius:0 5px 5px 0;background:#3b3b3b}
.stage{left:84px;top:90px;width:679px;height:336px;background:#f5f5f5;border:1px solid #e4e4e4;border-radius:8px}
.nav{left:0;top:102px;width:847px;height:32px;background:linear-gradient(#2ec0f5,#0b9ad8)}
.nav a{color:var(--white);font-family:"Source Sans 3",sans-serif;font-size:11.5px;font-weight:600;text-decoration:none;position:absolute;top:0;height:32px;line-height:32px;transform:translateX(-50%);white-space:nowrap}
.nav .sep{position:absolute;top:0;width:1px;height:32px;background:rgba(255,255,255,.25)}
.nav .active{background:rgba(0,0,0,.08);transform:none;left:211px;width:82px;text-align:center}
.menu{left:210px;top:134px;width:128px;background:rgba(50,50,50,.92);z-index:3}
.menu li{list-style:none;font-family:"Source Sans 3",sans-serif;font-size:10.5px;color:#d5d5d5;height:18.7px;line-height:18.7px;padding-left:16px;border-bottom:1px solid #4a4a4a;white-space:nowrap}
.hero{left:92px;top:144px;width:663px;height:271px;background:linear-gradient(100deg,#e9e4dc 0%,#d9cbb6 30%,#c79a6a 55%,#b8a27a 75%,#d6c8a8 100%)}
.dots{left:656px;top:390px;display:flex;gap:4px}
.dots i{width:13px;height:13px;border-radius:50%;background:var(--white);display:block}
.dots i:first-child{background:var(--blue)}
.card{background:var(--panel);border:1px solid var(--line);border-radius:3px}
.box{top:447px;width:211px;height:218px;padding:8px 13px}
.box h2{font-family:"Source Sans 3",sans-serif;font-weight:400;font-size:20px;line-height:24px;color:#555;margin-bottom:7px;white-space:nowrap}
.box p{font-size:9.3px;line-height:14px;margin-bottom:6px}
.benefits{list-style:none;margin-top:3px}
.benefits li{font-size:9.5px;font-weight:700;color:#555;height:18.6px;display:flex;align-items:center;gap:8px}
.benefits svg{flex:none}
.btn{position:absolute;left:13px;bottom:10px;width:62px;height:21px;background:linear-gradient(#27b7f1,#0b97d6);color:var(--white);font-size:10px;font-weight:700;text-align:center;line-height:21px;border-radius:2px}
.newsletter{left:0;top:679px;width:847px;height:52px;background:#f7f7f7;border-top:1px solid var(--line);border-bottom:1px solid var(--line)}
.newsletter h3{position:absolute;left:91px;top:13px;font-family:"Source Sans 3",sans-serif;font-weight:400;font-size:18px;color:#555}
.email{position:absolute;left:248px;top:14px;width:282px;height:20px;border:1px solid #c8c8c8;border-radius:3px;background:var(--white);font-size:9px;font-style:italic;color:#888;padding:4px 9px}
.subscribe{position:absolute;left:547px;top:14px;width:62px;height:20px;background:linear-gradient(#6a6a6a,#3a3a3a);color:var(--white);font-size:9.5px;font-weight:700;text-align:center;line-height:19px;border:1px solid #222;border-radius:2px}
.clients{left:92px;top:745px;width:437px;height:140px}
.news{left:544px;top:745px;width:211px;height:140px}
.panel-title{position:absolute;left:14px;top:8px;font-family:"Source Sans 3",sans-serif;font-weight:400;font-size:20px;color:#555}
.client-logo{position:absolute;top:52px;width:73px;height:35px;background:var(--white);border:1px solid #d6d6d6;font-size:9.5px;font-weight:700;color:#666;text-align:center;line-height:33px}
.date{position:absolute;left:14px;top:52px;width:40px;height:46px;border-radius:4px;background:#777;color:var(--white);text-align:center;font-family:"Source Sans 3",sans-serif}
.date .m{font-size:14px;line-height:18px}
.date .d{font-size:22px;font-weight:700;line-height:26px}
.news p{position:absolute;left:65px;top:48px;width:135px;font-size:9.3px;line-height:14.2px}
.read{position:absolute;right:14px;top:110px;font-size:9.5px;font-weight:700;color:var(--blue);text-decoration:underline}
.footer{left:0;top:904px;width:847px;height:296px;background:var(--footer)}
.fcol{position:absolute;top:16px}
.fcol h4{font-family:"Source Sans 3",sans-serif;font-weight:400;font-size:13px;line-height:16px;color:#e8e8e8}
.fcol li{list-style:none;font-size:8.6px;color:var(--footer-text);height:17px;display:flex;align-items:center;gap:5px;white-space:nowrap}
.fbrand{left:92px;top:148px;font-family:"Source Sans 3",sans-serif;font-size:40px;color:#8d8d8d;line-height:44px;letter-spacing:-1px}
.address{left:92px;top:200px;font-size:8.6px;line-height:14.2px;color:var(--footer-text)}
.address b{color:var(--white)}
.address .hi{color:var(--blue);font-size:10px}
.legal{right:92px;top:230px;text-align:right;font-size:8.6px;line-height:14.2px;color:var(--footer-text)}
.legal span{color:var(--white)}
</style>
</head>
<body>
<div class="page">

  <header>
    <div class="abs brand">tapnova<sup>TM</sup></div>
    <div class="abs tagline">contactless redemption for <b>mobile phones</b></div>
    <div class="abs search">Search...</div>
    <div class="abs search-btn">
      <svg width="26" height="20" viewBox="0 0 26 20"><circle cx="12" cy="9" r="4.5" fill="none" stroke="#fff" stroke-width="2"/><line x1="15.5" y1="12.5" x2="19" y2="16" stroke="#fff" stroke-width="2.4" stroke-linecap="round"/></svg>
    </div>
  </header>

  <div class="abs stage"></div>

  <nav class="abs nav">
    <svg class="abs" style="left:94px;top:9px" width="14" height="13" viewBox="0 0 14 13"><path d="M7 0 L14 6.5 H12 V13 H8.5 V9 H5.5 V13 H2 V6.5 H0 Z" fill="#fff"/></svg>
    <span class="sep" style="left:120px"></span>
    <a style="left:166px">About Tapnova</a>
    <span class="sep" style="left:211px"></span>
    <a class="active">Technology</a>
    <span class="sep" style="left:293px"></span>
    <a style="left:347px">Product Features</a>
    <span class="sep" style="left:402px"></span>
    <a style="left:432px">Clients</a>
    <span class="sep" style="left:462px"></span>
    <a style="left:505px">Latest News</a>
    <span class="sep" style="left:548px"></span>
    <a style="left:582px">Partners</a>
    <span class="sep" style="left:616px"></span>
    <a style="left:653px">Resellers</a>
    <span class="sep" style="left:690px"></span>
    <a style="left:729px">Contact Us</a>
  </nav>

  <div class="abs hero" role="img" aria-label="Photo of a shopper in a supermarket holding a basket of vegetables and checking her mobile phone"></div>
  <div class="abs dots"><i></i><i></i><i></i><i></i><i></i></div>

  <ul class="abs menu">
    <li>The Pod</li>
    <li>TheApp</li>
    <li>The SDK</li>
    <li>Reporting Interface</li>
    <li>Tapnova MD Interface</li>
    <li>Datamere Data Overlay</li>
  </ul>

  <section class="abs card box" style="left:92px">
    <h2>What is tapnova?</h2>
    <p>Lorem ipsum dolor sit amet, consec tetuer adipiscing elit. Praesent vestibulum mo lestie lacus. Aenean nonummy hendrerit mauris. Phasellus porta. Fusce suscipit varius mi.</p>
    <p>Lorem ipsum dolor sit amet, consec tetuer adipiscing elit. Praesent vestibulum mo lestie lacus.</p>
    <span class="btn">More</span>
  </section>

  <section class="abs card box" style="left:318px">
    <h2>How tapnova works?</h2>
    <p>Lorem ipsum dolor sit amet, consec tetuer adipiscing elit. Praesent vestibulum mo lestie lacus. Aenean nonummy hendrerit mauris. Phasellus porta. Fusce suscipit varius mi.</p>
    <p>Lorem ipsum dolor sit amet, consec tetuer adipiscing elit. Praesent vestibulum mo lestie lacus.</p>
    <span class="btn">More</span>
  </section>

  <section class="abs card box" style="left:544px">
    <h2>tapnova Key Benefits</h2>
    <p>Lorem ipsum dolor sit amet, consec tetuer adipiscing elit. Praesent vestibulum mo lestie lacus. Aenean nonummy hendrerit mauris. Phasellus porta.</p>
    <ul class="benefits">
      <li><svg width="9" height="9" viewBox="0 0 9 9"><circle cx="4.5" cy="4.5" r="4.5" fill="var(--red)"/><path d="M3.5 2.5 L5.5 4.5 L3.5 6.5" stroke="#fff" stroke-width="1.3" fill="none"/></svg>Mobile Coupon Redemption</li>
      <li><svg width="9" height="9" viewBox="0 0 9 9"><circle cx="4.5" cy="4.5" r="4.5" fill="var(--red)"/><path d="M3.5 2.5 L5.5 4.5 L3.5 6.5" stroke="#fff" stroke-width="1.3" fill="none"/></svg>Mobile Loyalty Cards</li>
      <li><svg width="9" height="9" viewBox="0 0 9 9"><circle cx="4.5" cy="4.5" r="4.5" fill="var(--red)"/><path d="M3.5 2.5 L5.5 4.5 L3.5 6.5" stroke="#fff" stroke-width="1.3" fill="none"/></svg>Mobile Check In</li>
      <li><svg width="9" height="9" viewBox="0 0 9 9"><circle cx="4.5" cy="4.5" r="4.5" fill="var(--red)"/><path d="M3.5 2.5 L5.5 4.5 L3.5 6.5" stroke="#fff" stroke-width="1.3" fill="none"/></svg>In Store Heat Maps</li>
    </ul>
    <span class="btn">More</span>
  </section>

  <section class="abs newsletter">
    <h3>Newsletter SignUp</h3>
    <div class="email">Enter Email Address</div>
    <div class="subscribe">Subscribe</div>
  </section>

  <section class="abs card clients">
    <h2 class="panel-title">tapnova Client’s</h2>
    <svg class="abs" style="left:4px;top:64px" width="8" height="12" viewBox="0 0 8 12"><path d="M6.5 1 L1.5 6 L6.5 11" stroke="#222" stroke-width="2" fill="none"/></svg>
    <div class="client-logo" style="left:18px">Cocoleaf</div>
    <div class="client-logo" style="left:100px">Crustworks</div>
    <div class="client-logo" style="left:182px">Coop Chicken</div>
    <div class="client-logo" style="left:264px">Fizzco</div>
    <div class="client-logo" style="left:346px">Ringmoor</div>
    <svg class="abs" style="left:424px;top:64px" width="8" height="12" viewBox="0 0 8 12"><path d="M1.5 1 L6.5 6 L1.5 11" stroke="#222" stroke-width="2" fill="none"/></svg>
  </section>

  <section class="abs card news">
    <h2 class="panel-title">tapnova News</h2>
    <svg class="abs" style="left:177px;top:15px" width="24" height="12" viewBox="0 0 24 12"><path d="M6.5 1 L1.5 6 L6.5 11 M17.5 1 L22.5 6 L17.5 11" stroke="#222" stroke-width="2" fill="none"/></svg>
    <div class="date"><div class="m">April</div><div class="d">29</div></div>
    <p>Lorem ipsum dolor sit amet, consec tetuer adipiscing elit. Praesent vestibulum mo lestie lacus.</p>
    <span class="read">Read More</span>
  </section>

  <footer class="abs footer">
    <div class="fcol" style="left:92px"><h4>Company Information</h4><ul><li>About Us</li><li>Services</li><li>Investor</li><li>News</li><li>Feedback Form</li><li>Contact Us</li></ul></div>
    <div class="fcol" style="left:267px"><h4>Clients</h4><ul><li>Case Studies</li><li>Client List</li><li>TapTrail</li></ul></div>
    <div class="fcol" style="left:371px"><h4>Partners</h4><ul><li>Case Studies</li><li>EPOS Partners</li></ul></div>
    <div class="fcol" style="left:482px"><h4>Technology</h4><ul><li>The Pod</li><li>The App</li><li>The SDK</li><li>Reporting Interface</li><li>Tapnova MI Interface</li><li>Datamere Data Overlay</li></ul></div>
    <div class="fcol" style="left:636px"><h4>Product Featured</h4><ul><li>Issuance / Redemption</li><li>Checkin</li><li>Loyalty</li><li>White Label App</li><li>SDK</li><li>Reporting</li><li>Point Of Sale Tag for Coupon</li></ul></div>
    <div class="fcol" style="left:317px;top:156px"><h4>Developer Section</h4><ul><li>SDK</li><li>Help Documentation</li><li>Register as a Developer</li></ul></div>
    <div class="fcol" style="left:482px;top:156px"><h4>Connect with Us</h4><ul>
      <li><svg width="10" height="10"><circle cx="5" cy="5" r="5" fill="#4aa3df"/></svg>Chirpline</li>
      <li><svg width="10" height="10"><circle cx="5" cy="5" r="5" fill="#4a6fb5"/></svg>Friendwall</li>
      <li><svg width="10" height="10"><circle cx="5" cy="5" r="5" fill="#3d84b8"/></svg>Workmesh</li>
    </ul></div>
    <div class="abs fbrand">tapnova</div>
    <div class="abs address">
      <b>Address</b><br>
      12 Harbour Lane, Glasgow, G01 4QX<br>
      Telephone: <span class="hi">+44 (0)161 555 0190</span><br>
      Fax: +44 (0)161 555 0191<br>
      Email:marketing@tapnova.example
    </div>
    <div class="abs legal">
      Copyright © 2012 by <span>tapnova</span><br>
      All Right Reserved<br>
      Terms and Conditions &nbsp;|&nbsp; Privacy Policy
    </div>
  </footer>

</div>
</body>
</html>
```